we need 5 posters for our restaurant. the posters will be based on a design template which I will provide in various formats. I will also provide the photos for the posters. so basically all that needs to be done is swapping over the photo from the current template and changing the price and menu item name to match the photo. we need 5 of these.

```html
<!DOCTYPE html>
<html lang="en">
<head>
<meta charset="utf-8">
<title>Harbor Grill – Poster Drafts</title>
<link rel="stylesheet" href="https://fonts.googleapis.com/css2?family=Montserrat:wght@800&family=Fredoka:wght@600&family=Gochi+Hand&display=swap">
<style>
  :root {
    --board: #e6e2e8;
    --ink: #0d0d0d;
    --paper: #ffffff;
    --sky: #3bb6ea;
    --sky-soft: #5fc4ee;
    --navy: #1457a5;
    --brand-blue: #2a5db0;
    --wood: #d8b584;
    --kraft: #bfa177;
    --wings-hi: #e38a3c;
    --wings-lo: #c8662c;
    --cream: #e9cfa4;
    --bun: #e2a962;
    --sauce: #c9432f;
    --meat: #6b4431;
  }
  * { box-sizing: border-box; margin: 0; padding: 0; }
  html, body { width: 1200px; height: 1200px; overflow: hidden; background: var(--board); }
  .board { position: relative; width: 1200px; height: 1200px; }
  .board-note {
    position: absolute; top: 134px; left: 0; width: 1200px;
    text-align: center; color: var(--ink);
    font-family: "Montserrat", sans-serif; font-weight: 800;
    font-size: 39px; line-height: 42px; letter-spacing: 0.07em; text-transform: uppercase;
  }
  .poster {
    position: absolute; top: 337px; width: 496px; height: 703px;
    background: var(--paper); overflow: hidden;
  }
  .poster--wings { left: 80px; }
  .poster--burger { left: 635px; }
  .poster-art { position: absolute; inset: 0; width: 496px; height: 703px; }
  .brand-name {
    position: absolute; left: 48px; top: 28px;
    font-family: "Fredoka", sans-serif; font-weight: 600;
    color: var(--brand-blue); font-size: 90px; line-height: 100px;
  }
  .price-badge {
    position: absolute; left: 22px; top: 535px; width: 132px; height: 132px;
    display: flex; align-items: center; justify-content: center; text-align: center;
    font-family: "Gochi Hand", cursive; color: var(--navy); text-transform: uppercase;
    font-size: 29px; line-height: 30px; transform: rotate(-10deg);
  }
  .tagline {
    position: absolute; left: 176px; top: 578px; width: 298px;
    font-family: "Fredoka", sans-serif; font-weight: 600; color: var(--paper);
    text-transform: uppercase; text-align: center;
  }
  .tagline-lead { display: block; font-size: 33px; line-height: 38px; letter-spacing: 0.05em; }
  .tagline-key { display: block; font-size: 72px; line-height: 72px; letter-spacing: 0.03em; }
</style>
</head>
<body>
<main class="board">
  <p class="board-note">This is just the first draft<br>I need prices so I can finish the designs</p>

  <article class="poster poster--wings">
    <svg class="poster-art" viewBox="0 0 496 703">
      <defs>
        <linearGradient id="wings-photo" x1="0" y1="0" x2="0" y2="1">
          <stop offset="0" stop-color="var(--cream)"/>
          <stop offset="0.25" stop-color="var(--wings-hi)"/>
          <stop offset="0.5" stop-color="var(--wings-lo)"/>
          <stop offset="0.72" stop-color="var(--kraft)"/>
          <stop offset="1" stop-color="var(--wood)"/>
        </linearGradient>
      </defs>
      <path class="sky-band" fill="var(--sky)" d="M0,250 L60,234 L120,222 L180,212 L230,200 L262,180 L300,162 L340,150 L380,138 L420,128 L460,116 L496,108 V400 H0Z"/>
      <g role="img" aria-label="Photo: fried chicken wings in a paper tray with a cup of ranch dip, burgers behind on a wooden table">
        <path fill="url(#wings-photo)" d="M0,215 L30,222 L60,214 L95,226 L130,218 L165,230 L200,222 L235,238 L270,236 L310,222 L360,218 L410,212 L460,214 L496,210 V560 H0Z"/>
      </g>
      <path class="base-band" fill="var(--navy)" d="M0,548 L30,540 L60,546 L100,532 L150,538 L200,528 L260,534 L320,527 L380,532 L430,524 L470,530 L496,522 V703 H0Z"/>
      <circle cx="88" cy="601" r="68" fill="var(--paper)" stroke="var(--navy)" stroke-width="3"/>
    </svg>
    <h2 class="brand-name">Harbor<br>Grill</h2>
    <p class="price-badge">Coast<br>Burger<br>9.90</p>
    <p class="tagline"><span class="tagline-lead">Classics for a</span><span class="tagline-key">Reason</span></p>
  </article>

  <article class="poster poster--burger">
    <svg class="poster-art" viewBox="0 0 496 703">
      <defs>
        <linearGradient id="burger-photo" x1="0" y1="0" x2="0" y2="1">
          <stop offset="0" stop-color="var(--sky-soft)"/>
          <stop offset="0.28" stop-color="var(--sky-soft)"/>
          <stop offset="0.45" stop-color="var(--bun)"/>
          <stop offset="0.62" stop-color="var(--sauce)"/>
          <stop offset="0.76" stop-color="var(--meat)"/>
          <stop offset="0.88" stop-color="var(--bun)"/>
          <stop offset="1" stop-color="var(--wood)"/>
        </linearGradient>
      </defs>
      <path class="sky-band" fill="var(--sky)" d="M0,250 L60,234 L120,222 L180,212 L230,200 L262,180 L300,162 L340,150 L380,138 L420,128 L460,116 L496,108 V400 H0Z"/>
      <g role="img" aria-label="Photo: cheeseburger with ketchup and mustard, a bowl of salad and another burger behind on a wooden table">
        <path fill="url(#burger-photo)" d="M0,230 L30,236 L60,228 L95,240 L130,232 L165,244 L200,236 L240,246 L290,244 L340,240 L400,238 L450,236 L496,232 V560 H0Z"/>
      </g>
      <path class="base-band" fill="var(--navy)" d="M0,548 L30,540 L60,546 L100,532 L150,538 L200,528 L260,534 L320,527 L380,532 L430,524 L470,530 L496,522 V703 H0Z"/>
      <circle cx="88" cy="601" r="68" fill="var(--paper)" stroke="var(--navy)" stroke-width="3"/>
    </svg>
    <h2 class="brand-name">Harbor<br>Grill</h2>
    <p class="price-badge">Coast<br>Burger<br>9.90</p>
    <p class="tagline"><span class="tagline-lead">Classics for a</span><span class="tagline-key">Reason</span></p>
  </article>
</main>
</body>
</html>
```